Ledger Paladin Powerpoint with Marshal Voltanic Type Theme

Need powerpoint template with matching colors and different slide options. Logo and colors to be used can be found at ledgerpaladinx.com. Want brightly colored slide deck that is readable form the back of a room, but highlights colors. I will be incorporating Tribbo into the slides to gamify my presentations.

Target Market(s)

Tech

Industry/Entity Type

IT, specifically database, but crossing over to mental health in IT, important note this is not for a company, this is just for a professional building a brand

Font styles to use
Sans Serif

Colors
0054AA
0677BA
7BADD7
CADEEF
E8F1F8
EB3D1F
EC4F4E
F09395
F8D3D4
FCEDEE

Requirements
Must have
• My Logo in the bottom corner, front page, a thank your page, question page, content page, content page with two columns, content page with graphs, and icons to be used in the primary colors of the logos, About Me Page, Break Slides, Demo break slide
Should not have
• Lighter shades of colors, I want to pop out where colors are used, I want spacing and font size to be readable from the back of a room, most likely black text and white background

```html
<!DOCTYPE html>
<html lang="en">
<head>
<meta charset="utf-8">
<title>Ledger Paladin – Slide Template Overview</title>
<link rel="stylesheet" href="https://fonts.googleapis.com/css2?family=Raleway:wght@300;400;500;600;700;800&display=swap">
<style>
:root{
  --navy:#1d3f80;
  --navy-deep:#16326a;
  --red:#e8262f;
  --charcoal:#3c3c3e;
  --grey:#8a8a8d;
  --ink:#4a4a4a;
  --canvas:#e7e7e7;
  --white:#ffffff;
  --faint:#dfe6f2;
}
*{box-sizing:border-box;margin:0;padding:0}
html,body{width:1200px;height:3178px;overflow:hidden}
body{background:var(--canvas);font-family:"Raleway",sans-serif;color:var(--ink)}
.deck{position:absolute;left:11px;top:11px;display:grid;grid-template-columns:repeat(3,387px);grid-auto-rows:217px;column-gap:8px;row-gap:8.7px}
.slide{position:relative;overflow:hidden;background:var(--white)}
.slide.navy{background:var(--navy)}
.slide.charcoal{background:var(--charcoal)}
.slide.red{background:var(--red)}
.abs{position:absolute}
.photo{position:absolute}
.brand{position:absolute;display:flex;align-items:center;gap:5px}
.brand-dot{width:15px;height:15px;border-radius:50%;background:var(--red);flex:none}
.brand-name{font-weight:800;font-size:10px;letter-spacing:.3px;color:var(--navy);text-transform:uppercase;line-height:1}
.brand.on-dark .brand-name{color:var(--white)}
.brand.on-red .brand-dot{background:var(--white)}
.brand.on-red .brand-name{color:var(--white)}
.edge-dot{position:absolute;right:3px;top:2px;width:11px;height:11px;border-radius:50%;background:var(--red)}
.edge-name{position:absolute;right:-28px;top:95px;transform:rotate(90deg);font-size:6px;font-weight:800;color:var(--red);text-transform:uppercase;white-space:nowrap;letter-spacing:.3px}
.page-no{position:absolute;right:8px;bottom:4px;font-size:4.5px;color:#888}
.title{font-weight:700;color:var(--navy);line-height:1.1}
.white{color:var(--white)}
.tiny{font-size:4.4px;line-height:1.5;color:#555}
.tiny.light{color:#dfe6f2}
.bar{display:block;width:14px;height:3px;background:var(--red);margin-top:5px}
.center{text-align:center}
.pill{position:absolute;border-radius:8px;background:var(--red);color:var(--white);font-size:5.5px;font-weight:600;display:flex;align-items:center;justify-content:center}
.card{position:absolute;color:var(--white);text-align:center;border-radius:2px}
.card h4{font-size:4.8px;font-weight:700;margin:4px 0 3px}
.card p{font-size:3.8px;line-height:1.45;padding:0 6px;color:#eef}
.icon-disc{position:absolute;width:22px;height:22px;border-radius:50%;background:var(--white);display:flex;align-items:center;justify-content:center;box-shadow:0 1px 3px rgba(0,0,0,.2)}
table{border-collapse:collapse}
.grid-table td,.grid-table th{font-size:4.6px;padding:3px 0;text-align:center;border-bottom:1px solid #e4e4e4;color:#777}
.grid-table th{background:var(--navy);color:var(--white);font-weight:700}
.grid-table td:first-child{font-weight:700;color:var(--navy)}
.big-num{font-weight:800;color:#d9d9d9;line-height:1}
.break-word{font-weight:300;color:var(--navy);line-height:.95}
</style>
</head>
<body>
<main class="deck">

<!-- 1 cover -->
<section class="slide navy">
  <div class="photo" role="img" aria-label="Dark blue tinted photo of hands using a tablet" style="inset:0;background:linear-gradient(135deg,#2a4f8f,#1a3670 60%,#132a58)"></div>
  <div class="brand on-dark" style="left:150px;top:38px"><span class="brand-dot"></span><span class="brand-name">Ledger Paladin</span></div>
  <p class="abs white center" style="left:0;right:0;top:68px;font-size:4.5px;letter-spacing:1px">www.ledgerpaladinx.com</p>
  <h1 class="abs white center" style="left:0;right:0;top:84px;font-size:25px;font-weight:700;line-height:1">Presentation<br>Title Goes Here</h1>
  <p class="abs white center" style="left:0;right:0;top:140px;font-size:8px">Sub Title Goes Here</p>
  <div class="pill" style="left:146px;top:176px;width:84px;height:12px">Oct 2021</div>
</section>

<!-- 2 -->
<section class="slide navy">
  <div class="photo" role="img" aria-label="Blue tinted photo of a person with a laptop" style="left:0;top:0;width:387px;height:180px;background:linear-gradient(120deg,#2b5190,#1d3f80 55%,#18346d)"></div>
  <h1 class="abs white" style="left:20px;top:70px;font-size:20px;font-weight:700;line-height:1.25">TITLE OF<br>PRESENTATION</h1>
  <p class="abs white" style="left:20px;top:136px;font-size:5px;line-height:1.4">Here is A place for Credentials<br>Date: 2021 March</p>
  <div class="abs" style="left:0;top:180px;width:387px;height:37px;background:var(--white)"></div>
  <div class="brand" style="left:10px;top:193px"><span class="brand-dot"></span><span class="brand-name">Ledger Paladin</span></div>
  <p class="abs" style="right:30px;top:199px;font-size:5px;font-weight:700;color:var(--navy)">Presenter Name</p>
</section>

<!-- 3 -->
<section class="slide navy">
  <div class="photo" role="img" aria-label="Blue tinted photo of a server room" style="inset:0;background:linear-gradient(90deg,#1b3a78,#244987 60%,#32599a)"></div>
  <div class="brand on-dark" style="left:24px;top:60px"><span class="brand-dot"></span><span class="brand-name">Ledger Paladin</span></div>
  <h1 class="abs white" style="left:24px;top:84px;font-size:20px;font-weight:700;line-height:1.25">TITLE OF<br>PRESENTATION</h1>
  <p class="abs white" style="left:24px;top:151px;font-size:5px;line-height:1.4">Here is A place for Credentials<br>Date: 2021 March</p>
</section>

<!-- 4 -->
<section class="slide">
  <div class="photo" role="img" aria-label="Photo of a laptop and hands on a desk" style="inset:0;background:linear-gradient(135deg,#c9ccd2,#8d96a6 55%,#5b6478)"></div>
  <svg class="abs" style="left:0;top:0" width="387" height="217" viewBox="0 0 387 217"><polygon points="0,0 230,0 115,217 0,217" fill="#1d3f80"/><polygon points="120,112 387,112 387,168 95,168" fill="#e8262f"/></svg>
  <div class="brand on-dark" style="left:40px;top:44px"><span class="brand-dot"></span><span class="brand-name" style="font-size:12px">Ledger Paladin</span></div>
  <h1 class="abs white center" style="left:140px;width:240px;top:118px;font-size:19px;font-weight:700;line-height:1">Presentation<br>Title Goes Here</h1>
</section>

<!-- 5 -->
<section class="slide">
  <div class="abs" style="left:220px;top:40px;width:140px;height:140px;border-radius:50%;border:10px solid var(--faint)"></div>
  <div class="brand" style="left:26px;top:45px"><span class="brand-dot"></span><span class="brand-name">Ledger Paladin</span></div>
  <h1 class="abs title" style="left:24px;top:82px;font-size:25px">Presentation<br>Title Goes Here</h1>
  <p class="abs" style="left:24px;top:134px;font-size:8px;color:var(--red)">Sub Title Goes Here</p>
  <div class="pill" style="left:20px;top:171px;width:118px;height:12px;font-size:4.5px;letter-spacing:1px">www.ledgerpaladinx.com</div>
</section>

<!-- 6 -->
<section class="slide">
  <div class="brand" style="left:140px;top:22px"><span class="brand-dot"></span><span class="brand-name">Ledger Paladin</span></div>
</section>

<!-- 7-9 -->
<section class="slide navy"><div class="brand on-dark" style="left:140px;top:22px"><span class="brand-dot"></span><span class="brand-name">Ledger Paladin</span></div></section>
<section class="slide charcoal"><div class="brand on-dark" style="left:140px;top:22px"><span class="brand-dot"></span><span class="brand-name">Ledger Paladin</span></div></section>
<section class="slide red"><div class="brand on-red" style="left:140px;top:22px"><span class="brand-dot"></span><span class="brand-name">Ledger Paladin</span></div></section>

<!-- 10 welcome -->
<section class="slide">
  <div class="photo" role="img" aria-label="Portrait photo of the presenter" style="left:29px;top:53px;width:110px;height:110px;border-radius:12px;background:linear-gradient(160deg,#6b6b6b,#2a2a2a)"></div>
  <div class="abs" style="left:29px;top:148px;width:110px;height:15px;background:var(--red);border-radius:0 0 12px 12px;color:#fff;font-size:7px;font-weight:700;text-align:center;line-height:15px">Your Name</div>
  <h2 class="abs title" style="left:175px;top:33px;font-size:17px">Welcome Message</h2>
  <p class="abs tiny" style="left:175px;top:60px;width:170px">Lorem ipsum dolor sit amet, consectetur adipiscing elit, sed do eiusmod tempor incididunt ut labore et dolore magna aliqua. Lorem ipsum dolor sit amet, consectetur adipiscing elit, sed do eiusmod tempor incididunt ut labore et dolore magna aliqua.</p>
  <p class="abs tiny" style="left:175px;top:101px;width:170px">Lorem ipsum dolor sit amet consectetur adipiscing elit sed do eiusmod tempor incididunt ut labore et dolore magna aliqua. Lorem ipsum dolor sit amet, consectetur adipiscing elit sed do eiusmod tempor incididunt ut labore et dolore magna aliqua. Lorem ipsum dolor sit amet consectetur adipiscing elit, sed do eiusmod tempor incididunt ut labore et dolore magna aliqua.</p>
  <span class="edge-dot"></span><span class="edge-name">Ledger Paladin</span><span class="page-no">10</span>
</section>

<!-- 11 profile -->
<section class="slide">
  <svg class="abs" style="left:16px;top:40px" width="40" height="70" viewBox="0 0 40 70"><g stroke="#1d3f80" stroke-width="4"><line x1="4" y1="30" x2="30" y2="4"/><line x1="4" y1="44" x2="38" y2="10"/><line x1="4" y1="58" x2="38" y2="24"/></g></svg>
  <div class="photo" role="img" aria-label="Round portrait photo of the manager" style="left:42px;top:40px;width:80px;height:80px;border-radius:50%;background:radial-gradient(circle at 50% 40%,#8a8a8a,#2d2d2d)"></div>
  <div class="abs" style="left:38px;top:142px;font-size:4px;color:var(--red);line-height:2.9">
    <div><span style="display:inline-block;width:6px;height:6px;border-radius:50%;background:var(--navy);margin-right:6px"></span>Here is a place for text</div>
    <div><span style="display:inline-block;width:6px;height:6px;border-radius:50%;background:var(--navy);margin-right:6px"></span>Here is a place for text</div>
    <div><span style="display:inline-block;width:6px;height:6px;background:var(--navy);margin-right:6px"></span>Here is a place for text</div>
  </div>
  <p class="abs" style="left:155px;top:30px;font-size:8px;color:var(--red)">Manager</p>
  <h2 class="abs title" style="left:155px;top:41px;font-size:16px">Name, Last Name</h2>
  <p class="abs tiny" style="left:155px;top:66px;width:190px"><span style="color:var(--red);font-weight:700">Lorem ipsum dolor sit amet, consectetur adipiscing elit,</span> sed do eiusmod tempor incididunt ut labore et dolore magna aliqua. Ut enim ad minim veniam, quis nostrud exercitation ullamco laboris nisi ut aliquip.</p>
  <p class="abs tiny" style="left:155px;top:104px;width:190px">Lorem ipsum dolor sit amet, consectetur adipiscing elit. Lorem ipsum dolor sit amet, consectetur adipiscing elit, sed do eiusmod tempor incididunt ut labore et dolore magna aliqua. Lorem ipsum dolor sit amet, consectetur adipiscing elit, sed do eiusmod tempor incididunt ut labore et dolore magna aliqua. Ut enim ad minim veniam, quis nostrud exercitation ullamco laboris nisi ut aliquip.</p>
  <span class="edge-dot"></span><span class="edge-name">Ledger Paladin</span><span class="page-no">11</span>
</section>

<!-- 12 agenda -->
<section class="slide">
  <div class="abs" style="left:0;top:0;width:150px;height:130px;background:var(--navy)"></div>
  <div class="abs" style="left:32px;top:30px;width:175px;height:165px;background:var(--white);box-shadow:0 2px 8px rgba(0,0,0,.12)"></div>
  <ol class="abs" style="left:52px;top:44px;font-size:6.5px;color:var(--navy);line-height:19px;padding-left:10px">
    <li>Lorem ipsum dolor sit amet</li><li>Lorem ipsum dolor sit amet</li><li>Lorem ipsum dolor sit amet</li><li>Lorem ipsum dolor sit amet</li><li>Lorem ipsum dolor sit amet</li><li>Lorem ipsum dolor sit amet</li><li>Lorem ipsum dolor sit amet</li>
  </ol>
  <h2 class="abs title" style="left:230px;top:74px;font-size:16px">Here Goes<br>Title Of Your<br>Agenda</h2>
  <p class="abs" style="left:230px;top:136px;font-size:6.5px;color:var(--red)">Here Goes A Short Subtitle</p>
  <span class="edge-dot"></span><span class="edge-name">Ledger Paladin</span><span class="page-no">12</span>
</section>

<!-- 13-15 title and body -->
<section class="slide">
  <div class="abs" style="left:140px;top:55px;width:110px;height:110px;border-radius:50%;border:10px solid var(--faint)"></div>
  <h2 class="abs title" style="left:14px;top:18px;font-size:15px">Title And Body Slide<span class="bar"></span></h2>
  <span class="edge-dot"></span><span class="edge-name">Ledger Paladin</span><span class="page-no">13</span>
</section>
<section class="slide">
  <h2 class="abs title" style="left:17px;top:18px;font-size:15px">Title And Body Slide<span class="bar"></span></h2>
  <span class="edge-dot"></span><span class="edge-name">Ledger Paladin</span><span class="page-no">14</span>
</section>
<section class="slide navy">
  <h2 class="abs title white" style="left:17px;top:16px;font-size:15px">Title And Body Slide<span class="bar"></span></h2>
  <span class="edge-dot"></span><span class="edge-name" style="color:#fff">Ledger Paladin</span><span class="page-no" style="color:#cfd8ea">15</span>
</section>

<!-- 16 -->
<section class="slide">
  <h2 class="abs title" style="left:17px;top:16px;font-size:15px">Title And Body Slide<span class="bar"></span></h2>
  <div class="abs tiny" style="left:17px;top:58px;width:330px">
    <p>Lorem ipsum dolor sit amet, consectetur adipiscing elit, sed do eiusmod tempor incididunt ut labore et dolore magna aliqua. Lorem ipsum dolor sit amet, consectetur adipiscing elit, sed do eiusmod tempor incididunt ut labore et dolore magna aliqua. Ut enim ad minim veniam, quis nostrud exercitation ullamco laboris nisi ut aliquip.</p><br>
    <p>Lorem ipsum dolor sit amet, consectetur adipiscing elit, sed do eiusmod tempor incididunt ut labore et dolore magna aliqua. Lorem ipsum dolor sit amet, consectetur adipiscing elit, sed do eiusmod tempor incididunt ut labore et dolore magna aliqua. Lorem ipsum dolor sit amet, consectetur adipiscing elit, sed do eiusmod tempor incididunt ut labore et dolore magna aliqua. Ut enim ad minim veniam, quis nostrud exercitation ullamco.</p><br>
    <p>Lorem ipsum dolor sit amet, consectetur adipiscing elit, sed do eiusmod tempor incididunt ut labore et dolore magna aliqua. Lorem ipsum dolor sit amet, consectetur adipiscing elit, sed do eiusmod tempor incididunt ut labore et dolore magna aliqua. Sed do eiusmod tempor incididunt ut labore et dolore magna aliqua. Lorem ipsum dolor sit amet, consectetur adipiscing elit, sed do eiusmod tempor incididunt ut labore et dolore magna aliqua. Ut enim ad minim veniam, quis nostrud exercitation ullamco laboris nisi.</p>
  </div>
  <span class="edge-dot"></span><span class="edge-name">Ledger Paladin</span><span class="page-no">16</span>
</section>

<!-- 17 break -->
<section class="slide">
  <span class="abs big-num" style="left:15px;top:50px;font-size:60px">01</span>
  <h2 class="abs break-word" style="left:36px;top:68px;font-size:31px">Slide<br>Break</h2>
  <p class="abs tiny" style="left:36px;top:140px;width:165px">Lorem ipsum dolor sit amet, consectetur adipiscing elit, sed do eiusmod tempor incididunt ut labore et dolore magna aliqua. Lorem ipsum dolor sit amet, consectetur adipiscing elit, sed do eiusmod tempor incididunt ut labore et dolore magna aliqua.</p>
  <div class="brand" style="left:220px;top:82px"><span class="brand-dot" style="width:30px;height:30px"></span><span class="brand-name" style="font-size:14px">Ledger<br>Paladin</span></div>
  <div class="abs" style="left:0;bottom:0;width:387px;height:9px;background:var(--red)"></div>
</section>

<!-- 18 -->
<section class="slide navy">
  <span class="abs big-num" style="left:22px;top:50px;font-size:60px;color:rgba(255,255,255,.25)">01</span>
  <h2 class="abs break-word white" style="left:43px;top:68px;font-size:31px">Slide<br>Break</h2>
  <p class="abs tiny light" style="left:43px;top:132px;width:165px">Lorem ipsum dolor sit amet, consectetur adipiscing elit, sed do eiusmod tempor incididunt ut labore et dolore magna aliqua. Lorem ipsum dolor sit amet, consectetur adipiscing elit, sed do eiusmod tempor incididunt ut labore et dolore magna aliqua.</p>
</section>

<!-- 19-21 demo -->
<section class="slide navy">
  <div class="photo" role="img" aria-label="Blue tinted photo of people at a laptop" style="inset:0;background:linear-gradient(120deg,#2a4f8e,#1d3f80)"></div>
  <div class="abs" style="left:103px;top:28px;width:180px;height:180px;border-radius:50%;border:1.5px solid #fff"></div>
  <p class="abs center" style="left:0;right:0;top:50px;font-size:16px;font-weight:700;color:var(--red)">DEMO</p>
  <p class="abs tiny light center" style="left:128px;width:130px;top:76px;font-size:5.4px">Lorem ipsum dolor sit amet, consectetur adipiscing elit, sed do eiusmod tempor incididunt ut labore et dolore magna aliqua. Lorem ipsum dolor sit amet, consectetur adipiscing elit, sed do eiusmod tempor incididunt ut magna aliqua. Lorem ipsum dolor sit amet, consectetur adipiscing elit, sed do eiusmod tempor incididunt ut labore et dolore magna aliqua. Lorem ipsum dolor sit amet.</p>
</section>
<section class="slide navy">
  <div class="abs" style="left:103px;top:28px;width:180px;height:180px;border-radius:50%;border:1.5px solid #fff"></div>
  <div class="abs" style="left:124px;top:50px;width:139px;height:3px"></div>
  <div class="abs" style="left:133px;top:57px;width:38px;height:1.5px;background:var(--red)"></div>
  <div class="abs" style="left:216px;top:57px;width:38px;height:1.5px;background:var(--red)"></div>
  <p class="abs center white" style="left:0;right:0;top:48px;font-size:16px;font-weight:700">DEMO</p>
  <p class="abs tiny light center" style="left:128px;width:130px;top:76px;font-size:5.4px">Lorem ipsum dolor sit amet, consectetur adipiscing elit, sed do eiusmod tempor incididunt ut labore et dolore magna aliqua. Lorem ipsum dolor sit amet, consectetur adipiscing elit, sed do eiusmod tempor incididunt ut magna aliqua. Lorem ipsum dolor sit amet, consectetur adipiscing elit, sed do eiusmod tempor incididunt ut labore et dolore magna aliqua. Lorem ipsum dolor sit amet.</p>
</section>
<section class="slide navy">
  <div class="photo" role="img" aria-label="Blue tinted photo of a laptop keyboard" style="inset:0;background:linear-gradient(90deg,#1d3f80,#2f5696)"></div>
  <div class="brand on-dark" style="left:24px;top:101px"><span class="brand-dot"></span><span class="brand-name">Ledger Paladin</span></div>
  <div class="abs" style="left:148px;top:70px;width:2px;height:85px;background:var(--red)"></div>
  <div class="pill" style="left:165px;top:69px;width:58px;height:15px;font-size:10px;font-weight:700">DEMO</div>
  <p class="abs tiny light" style="left:165px;top:92px;width:190px;font-size:6.3px">Lorem ipsum dolor sit amet, consectetur adipiscing elit, sed do eiusmod tempor incididunt ut labore et dolore magna aliqua. Lorem ipsum dolor sit amet, consectetur adipiscing elit, sed do eiusmod tempor incididunt ut labore et dolore magna aliqua.</p>
</section>

<!-- 22 pic and text -->
<section class="slide">
  <h2 class="abs title" style="left:38px;top:64px;font-size:20px">Pic And Text<span class="bar"></span></h2>
  <p class="abs tiny" style="left:38px;top:106px;width:135px;text-align:justify">Lorem ipsum dolor sit amet, consectetur adipiscing elit, sed do eiusmod tempor incididunt ut labore et dolore magna aliqua. Lorem ipsum dolor sit amet, consectetur adipiscing elit, sed do eiusmod tempor incididunt ut labore et dolore magna aliqua. Ut enim ad minim veniam, quis nostrud exercitation ullamco laboris nisi ut aliquip.</p>
  <div class="abs" style="left:190px;top:28px;width:110px;height:72px;background:var(--red)"></div>
  <div class="photo" role="img" aria-label="Photo of hands typing on a laptop" style="left:205px;top:45px;width:160px;height:135px;background:linear-gradient(150deg,#d7dbe2,#9aa2b1 60%,#6c7589)"></div>
  <span class="edge-dot"></span><span class="edge-name">Ledger Paladin</span><span class="page-no">22</span>
</section>

<!-- 23 -->
<section class="slide">
  <div class="photo" role="img" aria-label="Photo of a hiker standing on a mountain peak" style="left:0;top:0;width:168px;height:217px;background:linear-gradient(180deg,#9aa7b4,#5d6b78 50%,#2c3540)"></div>
  <div class="abs" style="left:190px;top:60px;width:40px;height:2px;background:var(--red)"></div>
  <p class="abs" style="left:190px;top:67px;width:165px;font-size:7.5px;font-weight:700;color:var(--navy);line-height:1.35">Success is not only what you achieve in your life, but also what you inspire in the lives of others</p>
  <div class="abs" style="left:100px;top:165px;width:287px;height:52px;background:var(--navy)"></div>
  <div class="abs" style="left:112px;top:175px;display:flex;gap:14px;color:#fff">
    <div style="width:80px"><b style="font-size:5px">Lorem ipsum dolor</b><p style="font-size:3.8px;margin-top:4px;line-height:1.4">Lorem ipsum dolor sit amet, consectetur adipiscing elit, sed do eiusmod tempor</p></div>
    <div style="width:80px"><b style="font-size:5px">Lorem ipsum dolor</b><p style="font-size:3.8px;margin-top:4px;line-height:1.4">Lorem ipsum dolor sit amet, consectetur adipiscing elit, sed do eiusmod tempor</p></div>
    <div style="width:80px"><b style="font-size:5px">Lorem ipsum dolor</b><p style="font-size:3.8px;margin-top:4px;line-height:1.4">Lorem ipsum dolor sit amet, consectetur adipiscing elit, sed do eiusmod tempor</p></div>
  </div>
  <span class="edge-dot"></span><span class="edge-name">Ledger Paladin</span>
</section>

<!-- 24 awesome text -->
<section class="slide">
  <div class="abs" style="left:0;top:0;width:365px;height:118px;background:var(--navy)"></div>
  <h2 class="abs white center" style="left:0;width:365px;top:32px;font-size:15px;font-weight:700">Here Add Awesome Text</h2>
  <div class="abs" style="left:0;width:365px;top:83px;display:flex;justify-content:space-around;text-align:center;padding:0 10px">
    <div style="width:105px"><div style="margin:0 auto;width:30px;height:30px;border-radius:50%;background:var(--red);border:3px solid #fff;display:flex;align-items:center;justify-content:center"><svg width="14" height="14" viewBox="0 0 14 14"><circle cx="7" cy="7" r="5.5" fill="none" stroke="#fff" stroke-width="1.2"/><circle cx="7" cy="7" r="2" fill="#fff"/></svg></div><p style="font-size:6px;font-weight:700;color:var(--navy);margin:6px 0 3px">Project name</p><p class="tiny" style="font-size:4px">Lorem ipsum dolor sit amet, nec an dictas equidem appellantur, ut has commune accommodare. Mea illum iudico soleat idque.</p></div>
    <div style="width:105px"><div style="margin:0 auto;width:30px;height:30px;border-radius:50%;background:var(--red);border:3px solid #fff;display:flex;align-items:center;justify-content:center"><svg width="14" height="14" viewBox="0 0 14 14"><path d="M3 11 L11 3 M11 3 L7 3 M11 3 L11 7" stroke="#fff" stroke-width="1.4" fill="none"/></svg></div><p style="font-size:6px;font-weight:700;color:var(--navy);margin:6px 0 3px">Project name</p><p class="tiny" style="font-size:4px">Lorem ipsum dolor sit amet, nec an dictas equidem appellantur, ut has commune accommodare. Mea illum iudico soleat idque.</p></div>
    <div style="width:105px"><div style="margin:0 auto;width:30px;height:30px;border-radius:50%;background:var(--red);border:3px solid #fff;display:flex;align-items:center;justify-content:center"><svg width="14" height="14" viewBox="0 0 14 14"><rect x="3" y="3" width="8" height="8" fill="none" stroke="#fff" stroke-width="1.2"/><line x1="3" y1="7" x2="11" y2="7" stroke="#fff" stroke-width="1.2"/></svg></div><p style="font-size:6px;font-weight:700;color:var(--navy);margin:6px 0 3px">Project name</p><p class="tiny" style="font-size:4px">Lorem ipsum dolor sit amet, nec an dictas equidem appellantur, ut has commune accommodare. Mea illum iudico soleat idque.</p></div>
  </div>
  <span class="edge-dot"></span><span class="edge-name">Ledger Paladin</span>
</section>

<!-- 25 three columns -->
<section class="slide">
  <h2 class="abs title center" style="left:0;width:370px;top:22px;font-size:15px">3 Columns Slide<span class="bar" style="margin:5px auto 0"></span></h2>
  <div class="card" style="left:43px;top:90px;width:90px;height:72px;background:var(--red)"><h4 style="margin-top:26px">Project name here</h4><p>Lorem ipsum dolor sit amet, nec an dictas equidem appellantur, ut has commune accommodare.</p></div>
  <div class="card" style="left:142px;top:90px;width:90px;height:72px;background:var(--navy)"><h4 style="margin-top:26px">Project name here</h4><p>Lorem ipsum dolor sit amet, nec an dictas equidem appellantur, ut has commune accommodare.</p></div>
  <div class="card" style="left:241px;top:90px;width:90px;height:72px;background:var(--grey)"><h4 style="margin-top:26px">Project name here</h4><p>Lorem ipsum dolor sit amet, nec an dictas equidem appellantur, ut has commune accommodare.</p></div>
  <div class="icon-disc" style="left:77px;top:79px"><svg width="11" height="11"><circle cx="5.5" cy="5.5" r="4" fill="none" stroke="#e8262f" stroke-width="1.3"/></svg></div>
  <div class="icon-disc" style="left:176px;top:79px"><svg width="11" height="11"><circle cx="5.5" cy="5.5" r="4" fill="none" stroke="#1d3f80" stroke-width="1.3"/><circle cx="5.5" cy="5.5" r="1.5" fill="#1d3f80"/></svg></div>
  <div class="icon-disc" style="left:275px;top:79px"><svg width="11" height="11"><circle cx="5.5" cy="5.5" r="4" fill="none" stroke="#8a8a8d" stroke-width="1.3"/></svg></div>
  <span class="edge-dot"></span><span class="edge-name">Ledger Paladin</span><span class="page-no">25</span>
</section>

<!-- 26 four columns -->
<section class="slide">
  <h2 class="abs title center" style="left:0;width:370px;top:22px;font-size:15px">4 Column Slide<span class="bar" style="margin:5px auto 0"></span></h2>
  <div class="card" style="left:20px;top:85px;width:80px;height:90px;background:var(--red)"><h4 style="margin-top:10px">Project name here</h4><p>Lorem ipsum dolor sit amet, nec an dictas equidem appellantur, ut has commune accommodare. Mea illum iudico soleat idque.</p></div>
  <div class="card" style="left:106px;top:85px;width:80px;height:90px;background:var(--navy)"><h4 style="margin-top:10px">Project name here</h4><p>Lorem ipsum dolor sit amet, nec an dictas equidem appellantur, ut has commune accommodare. Mea illum iudico soleat idque.</p></div>
  <div class="card" style="left:192px;top:85px;width:80px;height:90px;background:var(--navy-deep)"><h4 style="margin-top:10px">Project name here</h4><p>Lorem ipsum dolor sit amet, nec an dictas equidem appellantur, ut has commune accommodare. Mea illum iudico soleat idque.</p></div>
  <div class="card" style="left:278px;top:85px;width:80px;height:90px;background:var(--grey)"><h4 style="margin-top:10px">Project name here</h4><p>Lorem ipsum dolor sit amet, nec an dictas equidem appellantur, ut has commune accommodare. Mea illum iudico soleat idque.</p></div>
  <div class="icon-disc" style="left:49px;top:62px"><svg width="11" height="11"><circle cx="5.5" cy="5.5" r="4" fill="none" stroke="#e8262f" stroke-width="1.3"/></svg></div>
  <div class="icon-disc" style="left:135px;top:62px"><svg width="11" height="11"><path d="M5.5 1 V10 M2 7 Q5.5 11 9 7" fill="none" stroke="#1d3f80" stroke-width="1.2"/></svg></div>
  <div class="icon-disc" style="left:221px;top:62px"><svg width="11" height="11"><circle cx="5.5" cy="6" r="4" fill="none" stroke="#16326a" stroke-width="1.2"/><line x1="5.5" y1="6" x2="5.5" y2="3.5" stroke="#16326a" stroke-width="1.2"/></svg></div>
  <div class="icon-disc" style="left:307px;top:62px"><svg width="11" height="11"><circle cx="3" cy="6" r="2.5" fill="none" stroke="#8a8a8d"/><circle cx="8" cy="6" r="2.5" fill="none" stroke="#8a8a8d"/></svg></div>
  <span class="edge-dot"></span><span class="edge-name">Ledger Paladin</span><span class="page-no">26</span>
</section>

<!-- 27 five columns -->
<section class="slide">
  <h2 class="abs title center" style="left:0;width:370px;top:22px;font-size:15px">5 Column Slide<span class="bar" style="margin:5px auto 0"></span></h2>
  <div class="card" style="left:43px;top:65px;width:92px;height:57px;background:var(--navy)"><h4 style="margin-top:8px">Project name here</h4><p>Lorem ipsum dolor sit amet, nec an dictas equidem appellantur, ut has commune accommodare. Mea illum iudico soleat idque.</p></div>
  <div class="card" style="left:142px;top:65px;width:92px;height:57px;background:var(--navy)"><h4 style="margin-top:8px">Project name here</h4><p>Lorem ipsum dolor sit amet, nec an dictas equidem appellantur, ut has commune accommodare. Mea illum iudico soleat idque.</p></div>
  <div class="card" style="left:241px;top:65px;width:92px;height:57px;background:var(--navy)"><h4 style="margin-top:8px">Project name here</h4><p>Lorem ipsum dolor sit amet, nec an dictas equidem appellantur, ut has commune accommodare. Mea illum iudico soleat idque.</p></div>
  <div class="card" style="left:92px;top:130px;width:92px;height:57px;background:var(--navy)"><h4 style="margin-top:8px">Project name here</h4><p>Lorem ipsum dolor sit amet, nec an dictas equidem appellantur, ut has commune accommodare. Mea illum iudico soleat idque.</p></div>
  <div class="card" style="left:191px;top:130px;width:92px;height:57px;background:var(--navy)"><h4 style="margin-top:8px">Project name here</h4><p>Lorem ipsum dolor sit amet, nec an dictas equidem appellantur, ut has commune accommodare. Mea illum iudico soleat idque.</p></div>
  <span class="edge-dot"></span><span class="edge-name">Ledger Paladin</span><span class="page-no">27</span>
</section>

<!-- 28 screenshot -->
<section class="slide">
  <svg class="abs" style="left:0;top:0" width="387" height="217" viewBox="0 0 387 217"><polygon points="0,0 135,0 290,217 0,217" fill="#1d3f80"/></svg>
  <h2 class="abs white" style="left:18px;top:68px;font-size:16px;font-weight:700;line-height:1.15">A Place for<br>Screenshot<span class="bar"></span></h2>
  <p class="abs tiny light" style="left:18px;top:124px;width:120px">Lorem ipsum dolor sit amet, consectetur adipiscing elit, sed do eiusmod tempor elit, beta ex ipsum dolor dolor sit ke it.</p>
  <div class="abs" style="left:153px;top:48px;width:210px;height:125px;background:#2b2b2b;border-radius:6px 6px 0 0;padding:7px"><div style="width:100%;height:100%;background:#8c8c8c;display:flex;align-items:center;justify-content:center;color:#fff;font-size:6px;font-weight:600">HERE YOU CAN ADD A SCREENSHOT</div></div>
  <div class="abs" style="left:140px;top:173px;width:236px;height:6px;background:#c9c9c9;border-radius:0 0 6px 6px"></div>
  <span class="edge-dot"></span><span class="edge-name">Ledger Paladin</span><span class="page-no">28</span>
</section>

<!-- 29 six columns -->
<section class="slide">
  <h2 class="abs title center" style="left:0;width:370px;top:22px;font-size:15px">6 Columns Slide<span class="bar" style="margin:5px auto 0"></span></h2>
  <div class="abs" style="left:30px;top:70px;display:grid;grid-template-columns:160px 160px;row-gap:12px;column-gap:10px">
    <div style="display:flex;gap:14px"><svg width="14" height="14" style="margin-top:4px"><rect x="1" y="1" width="12" height="12" fill="none" stroke="#1d3f80"/><line x1="4" y1="5" x2="10" y2="5" stroke="#1d3f80"/><line x1="4" y1="9" x2="10" y2="9" stroke="#1d3f80"/></svg><div><p style="font-size:4.8px;font-weight:700;color:var(--navy)">Project name</p><p class="tiny" style="font-size:4px">Lorem ipsum dolor sit amet, nec an dictas equidem appellantur, ut has commune accommodare. Mea illum iudico soleat idque.</p></div></div>
    <div style="display:flex;gap:14px"><svg width="14" height="14" style="margin-top:4px"><rect x="1" y="1" width="12" height="12" fill="none" stroke="#1d3f80"/><line x1="4" y1="5" x2="10" y2="5" stroke="#1d3f80"/><line x1="4" y1="9" x2="10" y2="9" stroke="#1d3f80"/></svg><div><p style="font-size:4.8px;font-weight:700;color:var(--navy)">Project name</p><p class="tiny" style="font-size:4px">Lorem ipsum dolor sit amet, nec an dictas equidem appellantur, ut has commune accommodare. Mea illum iudico soleat idque.</p></div></div>
    <div style="display:flex;gap:14px"><svg width="14" height="14" style="margin-top:4px"><rect x="2" y="8" width="2.5" height="5" fill="#1d3f80"/><rect x="6" y="5" width="2.5" height="8" fill="#1d3f80"/><rect x="10" y="2" width="2.5" height="11" fill="#1d3f80"/></svg><div><p style="font-size:4.8px;font-weight:700;color:var(--navy)">Project name</p><p class="tiny" style="font-size:4px">Lorem ipsum dolor sit amet, nec an dictas equidem appellantur, ut has commune accommodare. Mea illum iudico soleat idque.</p></div></div>
    <div style="display:flex;gap:14px"><svg width="14" height="14" style="margin-top:4px"><rect x="2" y="8" width="2.5" height="5" fill="#1d3f80"/><rect x="6" y="5" width="2.5" height="8" fill="#1d3f80"/><rect x="10" y="2" width="2.5" height="11" fill="#1d3f80"/></svg><div><p style="font-size:4.8px;font-weight:700;color:var(--navy)">Project name</p><p class="tiny" style="font-size:4px">Lorem ipsum dolor sit amet, nec an dictas equidem appellantur, ut has commune accommodare. Mea illum iudico soleat idque.</p></div></div>
    <div style="display:flex;gap:14px"><svg width="14" height="14" style="margin-top:4px"><circle cx="7" cy="7" r="5.5" fill="none" stroke="#1d3f80"/><circle cx="7" cy="7" r="2" fill="#1d3f80"/></svg><div><p style="font-size:4.8px;font-weight:700;color:var(--navy)">Project name</p><p class="tiny" style="font-size:4px">Lorem ipsum dolor sit amet, nec an dictas equidem appellantur, ut has commune accommodare. Mea illum iudico soleat idque.</p></div></div>
    <div style="display:flex;gap:14px"><svg width="14" height="14" style="margin-top:4px"><circle cx="7" cy="7" r="5.5" fill="none" stroke="#1d3f80"/><circle cx="7" cy="7" r="2" fill="#1d3f80"/></svg><div><p style="font-size:4.8px;font-weight:700;color:var(--navy)">Project name</p><p class="tiny" style="font-size:4px">Lorem ipsum dolor sit amet, nec an dictas equidem appellantur, ut has commune accommodare. Mea illum iudico soleat idque.</p></div></div>
  </div>
  <span class="edge-dot"></span><span class="edge-name">Ledger Paladin</span><span class="page-no">29</span>
</section>

<!-- 30 table with ticks -->
<section class="slide">
  <h2 class="abs title center" style="left:0;width:370px;top:18px;font-size:15px">Table Slide<span class="bar" style="margin:5px auto 0"></span></h2>
  <table class="abs" style="left:18px;top:58px;width:345px;font-size:4.5px">
    <tr style="height:13px"><td style="width:97px"></td><td style="background:var(--red);color:#fff;font-weight:700;text-align:center">Your Text Here</td><td style="background:var(--red);color:#fff;font-weight:700;text-align:center">Your Text Here</td><td style="background:var(--red);color:#fff;font-weight:700;text-align:center">Your Text Here</td><td style="background:var(--red);color:#fff;font-weight:700;text-align:center">Your Text Here</td></tr>
    <tr style="height:17px"><td style="background:var(--navy);color:#fff;font-weight:700;padding-left:12px">You can replace this text</td><td class="center" style="color:#999">sfdgf</td><td class="center" style="color:var(--navy);font-size:8px">✔</td><td class="center" style="color:#999">gsfd</td><td class="center" style="color:#999">sdgs</td></tr>
    <tr style="height:17px"><td style="background:var(--navy);color:#fff;font-weight:700;padding-left:12px">You can replace this text</td><td class="center" style="color:#999">gfsdg</td><td class="center" style="color:var(--navy);font-size:8px">✖</td><td class="center" style="color:#999">sdfg</td><td class="center" style="color:#999">dsfg</td></tr>
    <tr style="height:17px"><td style="background:var(--navy);color:#fff;font-weight:700;padding-left:12px">You can replace this text</td><td class="center" style="color:#999">sdfsd</td><td class="center" style="color:var(--navy);font-size:8px">✔</td><td class="center" style="color:#999">sdfs</td><td class="center" style="color:#999">sdfsg</td></tr>
    <tr style="height:17px"><td style="background:var(--navy);color:#fff;font-weight:700;padding-left:12px">You can replace this text</td><td class="center" style="color:#999">fsfd</td><td class="center" style="color:var(--navy);font-size:8px">✖</td><td class="center" style="color:#999">fgsd</td><td class="center" style="color:#999">fsdf</td></tr>
    <tr style="height:17px"><td style="background:var(--navy);color:#fff;font-weight:700;padding-left:12px">You can replace this text</td><td class="center" style="color:#999">sgsd</td><td class="center" style="color:var(--navy);font-size:8px">✔</td><td class="center" style="color:#999">gsdf</td><td class="center" style="color:#999">sgsd</td></tr>
    <tr style="height:17px"><td style="background:var(--navy);color:#fff;font-weight:700;padding-left:12px">You can replace this text</td><td class="center" style="color:#999">gfsd</td><td class="center" style="color:var(--navy);font-size:8px">✖</td><td class="center" style="color:#999">gsdf</td><td class="center" style="color:#999">gfsd</td></tr>
    <tr style="height:17px"><td style="background:var(--navy);color:#fff;font-weight:700;padding-left:12px">You can replace this text</td><td class="center" style="color:#999">sdfd</td><td class="center" style="color:var(--navy);font-size:8px">✖</td><td class="center" style="color:#999">sdfs</td><td class="center" style="color:#999">dfsd</td></tr>
  </table>
  <span class="edge-dot"></span><span class="edge-name">Ledger Paladin</span><span class="page-no">30</span>
</section>

<!-- 31 table with side panel -->
<section class="slide">
  <div class="abs" style="left:0;top:0;width:207px;height:217px;background:var(--navy)"></div>
  <h2 class="abs white" style="left:17px;top:98px;font-size:16px;font-weight:700">Table Slide<span class="bar"></span></h2>
  <div class="abs" style="left:138px;top:34px;width:222px;height:160px;background:#fff;border-radius:6px;box-shadow:0 2px 10px rgba(0,0,0,.18)"></div>
  <table class="abs grid-table" style="left:150px;top:48px;width:198px">
    <tr><th>Text</th><th>Text</th><th>Text</th><th>Text</th><th>Text</th></tr>
    <tr><td>Data</td><td>Data</td><td>Data</td><td>Data</td><td>Data</td></tr>
    <tr><td>Data</td><td>Data</td><td>Data</td><td>Data</td><td>Data</td></tr>
    <tr><td>Data</td><td>Data</td><td>Data</td><td>Data</td><td>Data</td></tr>
    <tr><td>Data</td><td>Data</td><td>Data</td><td>Data</td><td>Data</td></tr>
    <tr><td>Data</td><td>Data</td><td>Data</td><td>Data</td><td>Data</td></tr>
    <tr><td>Data</td><td>Data</td><td>Data</td><td>Data</td><td>Data</td></tr>
  </table>
  <span class="edge-dot"></span><span class="edge-name">Ledger Paladin</span><span class="page-no">31</span>
</section>

<!-- 32 table -->
<section class="slide">
  <h2 class="abs title center" style="left:0;width:370px;top:20px;font-size:15px">Table Slide<span class="bar" style="margin:5px auto 0"></span></h2>
  <table class="abs grid-table" style="left:30px;top:63px;width:318px">
    <tr><th>Text</th><th>Text</th><th>Text</th><th>Text</th><th>Text</th></tr>
    <tr><td>Data</td><td>Data</td><td>Data</td><td>Data</td><td>Data</td></tr>
    <tr><td>Data</td><td>Data</td><td>Data</td><td>Data</td><td>Data</td></tr>
    <tr><td>Data</td><td>Data</td><td>Data</td><td>Data</td><td>Data</td></tr>
    <tr><td>Data</td><td>Data</td><td>Data</td><td>Data</td><td>Data</td></tr>
    <tr><td>Data</td><td>Data</td><td>Data</td><td>Data</td><td>Data</td></tr>
    <tr><td>Data</td><td>Data</td><td>Data</td><td>Data</td><td>Data</td></tr>
  </table>
  <span class="edge-dot"></span><span class="edge-name">Ledger Paladin</span><span class="page-no">32</span>
</section>

<!-- 33 smart art -->
<section class="slide">
  <h2 class="abs title" style="left:20px;top:15px;font-size:15px">Smart Art Slide<span class="bar"></span></h2>
  <div class="abs" style="left:22px;top:65px;display:flex;flex-direction:column;gap:16px;width:170px">
    <div style="display:flex;gap:10px"><svg width="12" height="12" style="margin-top:4px"><circle cx="6" cy="6" r="5" fill="none" stroke="#1d3f80"/></svg><div><p style="font-size:4.8px;font-weight:700;color:var(--navy)">Lorem ipsum dolor</p><p class="tiny" style="font-size:3.9px">Lorem ipsum dolor sit amet, consectetur adipiscing elit, sed do eiusmod tempor ut labore et dolore dolor sit.</p></div></div>
    <div style="display:flex;gap:10px"><svg width="12" height="12" style="margin-top:4px"><path d="M2 10 L10 2" stroke="#1d3f80" stroke-width="1.3"/></svg><div><p style="font-size:4.8px;font-weight:700;color:var(--navy)">Lorem ipsum dolor</p><p class="tiny" style="font-size:3.9px">Lorem ipsum dolor sit amet, consectetur adipiscing elit, sed do eiusmod tempor ut labore et dolore dolor sit.</p></div></div>
    <div style="display:flex;gap:10px"><svg width="12" height="12" style="margin-top:4px"><rect x="1" y="1" width="10" height="10" fill="none" stroke="#1d3f80"/></svg><div><p style="font-size:4.8px;font-weight:700;color:var(--navy)">Lorem ipsum dolor</p><p class="tiny" style="font-size:3.9px">Lorem ipsum dolor sit amet, consectetur adipiscing elit, sed do eiusmod tempor ut labore et dolore dolor sit.</p></div></div>
  </div>
  <svg class="abs" style="left:195px;top:40px" width="170" height="160" viewBox="0 0 170 160"><polygon points="85,0 130,78 40,78" fill="#1d3f80"/><polygon points="38,82 83,160 0,160" fill="#e8262f" transform="translate(-2,0)"/><polygon points="132,82 170,160 88,160" fill="#8a8a8d"/></svg>
  <p class="abs white center" style="left:255px;top:75px;width:50px;font-size:4.8px;font-weight:700">Project name</p>
  <p class="abs white center" style="left:250px;top:89px;width:60px;font-size:3.6px;line-height:1.4">Lorem ipsum dolor sit amet, nec an dictas equidem</p>
  <p class="abs white center" style="left:205px;top:158px;width:50px;font-size:4.8px;font-weight:700">Project name</p>
  <p class="abs white center" style="left:200px;top:169px;width:60px;font-size:3.6px;line-height:1.4">Lorem ipsum dolor sit amet, nec an dictas equidem</p>
  <p class="abs white center" style="left:298px;top:158px;width:50px;font-size:4.8px;font-weight:700">Project name</p>
  <p class="abs white center" style="left:293px;top:169px;width:60px;font-size:3.6px;line-height:1.4">Lorem ipsum dolor sit amet, nec an dictas equidem</p>
  <span class="edge-dot"></span><span class="edge-name">Ledger Paladin</span><span class="page-no">33</span>
</section>

<!-- 34 quotes -->
<section class="slide">
  <h2 class="abs title center" style="left:0;width:370px;top:18px;font-size:15px">Here is Quotes<span class="bar" style="margin:5px auto 0"></span></h2>
  <p class="abs" style="left:29px;top:52px;font-size:34px;font-weight:800;color:var(--red);line-height:1">”</p>
  <p class="abs" style="left:207px;top:52px;font-size:34px;font-weight:800;color:var(--navy);line-height:1">”</p>
  <p class="abs" style="left:29px;top:97px;width:150px;font-size:5.8px;line-height:1.6;color:#444">Lorem ipsum dolor sit amet, consectetur adipiscing elit, sed do eiusmod tempor incididunt ut labore et dolore magna aliqua. Lorem ipsum dolor sit amet, consectetur adipiscing elit.</p>
  <p class="abs" style="left:207px;top:97px;width:150px;font-size:5.8px;line-height:1.6;color:#444">Lorem ipsum dolor sit amet, consectetur adipiscing elit, sed do eiusmod tempor incididunt ut labore et dolore magna aliqua. Lorem ipsum dolor sit amet, consectetur adipiscing elit.</p>
  <div class="abs" style="left:29px;top:163px;display:flex;gap:6px;align-items:center"><span style="width:17px;height:17px;border-radius:50%;background:#ddd"></span><span style="font-size:4.8px;color:var(--navy);font-weight:700;line-height:1.5">Your Name<br><span style="font-weight:400;color:#888">Founder</span></span></div>
  <div class="abs" style="left:207px;top:163px;display:flex;gap:6px;align-items:center"><span style="width:17px;height:17px;border-radius:50%;background:#ddd"></span><span style="font-size:4.8px;color:var(--navy);font-weight:700;line-height:1.5">Your Name<br><span style="font-weight:400;color:#888">Founder</span></span></div>
  <span class="edge-dot"></span><span class="edge-name">Ledger Paladin</span><span class="page-no">34</span>
</section>

<!-- 35 statistics -->
<section class="slide">
  <h2 class="abs title center" style="left:0;width:370px;top:18px;font-size:15px">Here Is Statistics<span class="bar" style="margin:5px auto 0"></span></h2>
  <svg class="abs" style="left:20px;top:60px" width="160" height="130" viewBox="0 0 160 130">
    <circle cx="60" cy="65" r="58" fill="#1d3f80"/>
    <circle cx="60" cy="80" r="42" fill="#e8262f"/>
    <circle cx="60" cy="100" r="22" fill="#8a8a8d"/>
    <g fill="#fff" font-family="Raleway,sans-serif" font-weight="800" text-anchor="middle"><text x="60" y="30" font-size="18">$</text><text x="60" y="66" font-size="16">$</text><text x="60" y="106" font-size="12">$</text></g>
    <g stroke="#999" stroke-width=".6"><line x1="80" y1="23" x2="128" y2="23"/><line x1="95" y1="60" x2="128" y2="60"/><line x1="80" y1="100" x2="128" y2="100"/></g>
    <g font-family="Raleway,sans-serif" font-weight="700" font-size="9" fill="#1d3f80"><text x="132" y="26">5M</text><text x="132" y="63">2M</text><text x="132" y="103">1M</text></g>
  </svg>
  <div class="abs" style="left:205px;top:78px;display:flex;flex-direction:column;gap:12px;width:140px">
    <div style="display:flex;gap:8px"><span style="flex:none;width:11px;height:11px;background:var(--navy);color:#fff;font-size:8px;text-align:center;line-height:11px">✓</span><div><p style="font-size:5px;font-weight:700;color:var(--navy)">Lorem ipsum dolor</p><p class="tiny" style="font-size:4px">Lorem ipsum dolor sit amet, consectetur adipiscing elit, sed do eiusmod tempor</p></div></div>
    <div style="display:flex;gap:8px"><span style="flex:none;width:11px;height:11px;background:var(--red);color:#fff;font-size:8px;text-align:center;line-height:11px">✓</span><div><p style="font-size:5px;font-weight:700;color:var(--navy)">Lorem ipsum dolor</p><p class="tiny" style="font-size:4px">Lorem ipsum dolor sit amet, consectetur adipiscing elit, sed do eiusmod tempor</p></div></div>
    <div style="display:flex;gap:8px"><span style="flex:none;width:11px;height:11px;background:var(--charcoal);color:#fff;font-size:8px;text-align:center;line-height:11px">✓</span><div><p style="font-size:5px;font-weight:700;color:var(--navy)">Lorem ipsum dolor</p><p class="tiny" style="font-size:4px">Lorem ipsum dolor sit amet, consectetur adipiscing elit, sed do eiusmod tempor</p></div></div>
  </div>
  <span class="edge-dot"></span><span class="edge-name">Ledger Paladin</span><span class="page-no">35</span>
</section>

<!-- 36 rings -->
<section class="slide">
  <h2 class="abs title center" style="left:0;width:370px;top:18px;font-size:15px">Here Add Your Title<span class="bar" style="margin:5px auto 0"></span></h2>
  <p class="abs tiny center" style="left:60px;width:250px;top:58px">Lorem ipsum the printing and typesetting industry. Lorem ipsum has been the industry's standard dummy text ever since the 1500s, when an unknown printer took a galley of type and scrambled it to make a type specimen book. It has survived not only five centuries.</p>
  <svg class="abs" style="left:60px;top:100px" width="260" height="60" viewBox="0 0 260 60" font-family="Raleway,sans-serif" font-weight="700" font-size="12" text-anchor="middle">
    <circle cx="40" cy="30" r="24" fill="none" stroke="#e0e0e0" stroke-width="3"/><circle cx="40" cy="30" r="24" fill="none" stroke="#1d3f80" stroke-width="3" stroke-dasharray="75.4 150.8" transform="rotate(-90 40 30)"/><text x="40" y="34" fill="#1d3f80">50%</text>
    <circle cx="130" cy="30" r="24" fill="none" stroke="#e0e0e0" stroke-width="3"/><circle cx="130" cy="30" r="24" fill="none" stroke="#e8262f" stroke-width="3" stroke-dasharray="113 150.8" transform="rotate(-90 130 30)"/><text x="130" y="34" fill="#e8262f">75%</text>
    <circle cx="220" cy="30" r="24" fill="none" stroke="#e0e0e0" stroke-width="3"/><circle cx="220" cy="30" r="24" fill="none" stroke="#1d3f80" stroke-width="3" stroke-dasharray="60.3 150.8" transform="rotate(-90 220 30)"/><text x="220" y="34" fill="#1d3f80">40%</text>
  </svg>
  <div class="abs tiny center" style="left:70px;top:166px;width:250px;display:flex;justify-content:space-between"><span style="width:60px">Lorem ipsum dolor sit amet consectetur dolor</span><span style="width:60px">Lorem ipsum dolor sit amet consectetur dolor</span><span style="width:60px">Lorem ipsum dolor sit amet consectetur dolor</span></div>
  <span class="edge-dot"></span><span class="edge-name">Ledger Paladin</span><span class="page-no">36</span>
</section>

<!-- 37 line chart -->
<section class="slide">
  <h2 class="abs title center" style="left:0;width:370px;top:18px;font-size:15px">Here is Statistics<span class="bar" style="margin:5px auto 0"></span></h2>
  <div class="abs" style="left:16px;top:70px;width:88px;height:48px;background:var(--navy);color:#fff;text-align:center;padding-top:12px"><p style="font-size:14px;font-weight:500">$0.5M</p><p style="font-size:4px">Revenue</p></div>
  <div class="abs" style="left:16px;top:124px;width:88px;height:48px;background:#fff;box-shadow:0 1px 5px rgba(0,0,0,.15);color:var(--red);text-align:center;padding-top:12px"><p style="font-size:14px;font-weight:500">-0.28%</p><p style="font-size:4px">Revenue</p></div>
  <svg class="abs" style="left:120px;top:68px" width="245" height="120" viewBox="0 0 245 120" font-family="Raleway,sans-serif" font-size="4" fill="#888">
    <g stroke="#eee" stroke-width=".6"><line x1="25" y1="8" x2="245" y2="8"/><line x1="25" y1="24" x2="245" y2="24"/><line x1="25" y1="40" x2="245" y2="40"/><line x1="25" y1="56" x2="245" y2="56"/><line x1="25" y1="72" x2="245" y2="72"/><line x1="25" y1="88" x2="245" y2="88"/><line x1="25" y1="104" x2="245" y2="104"/></g>
    <text x="0" y="10">$600,000</text><text x="0" y="26">$500,000</text><text x="0" y="42">$400,000</text><text x="0" y="58">$300,000</text><text x="0" y="74">$200,000</text><text x="0" y="90">$100,000</text><text x="14" y="106">0</text>
    <path d="M28 100 C45 98 55 90 70 92 S90 80 100 60 S115 58 125 75 S140 55 150 62 S165 80 175 72 S190 45 200 55 S215 60 222 40 S235 20 240 15" fill="none" stroke="#e8262f" stroke-width="1.2"/>
    <g text-anchor="middle"><text x="30" y="114">Jan</text><text x="48" y="114">Feb</text><text x="66" y="114">Mar</text><text x="84" y="114">Apr</text><text x="102" y="114">May</text><text x="120" y="114">Jun</text><text x="138" y="114">Jul</text><text x="156" y="114">Aug</text><text x="174" y="114">Sep</text><text x="192" y="114">Oct</text><text x="210" y="114">Nov</text><text x="228" y="114">Dec</text></g>
  </svg>
  <span class="edge-dot"></span><span class="edge-name">Ledger Paladin</span><span class="page-no">37</span>
</section>

<!-- 38 timeline -->
<section class="slide">
  <h2 class="abs title center" style="left:0;width:370px;top:18px;font-size:15px">Company Timeline<span class="bar" style="margin:5px auto 0"></span></h2>
  <svg class="abs" style="left:22px;top:80px" width="335" height="40" viewBox="0 0 335 40" font-family="Raleway,sans-serif" font-size="7" font-weight="700" fill="#fff" text-anchor="middle">
    <polygon points="0,6 55,6 67,20 55,34 0,34 12,20" fill="#e8262f"/><text x="34" y="23">STEP 01</text>
    <polygon points="63,6 118,6 130,20 118,34 63,34 75,20" fill="#1d3f80"/><text x="97" y="23">STEP 02</text>
    <polygon points="126,6 181,6 193,20 181,34 126,34 138,20" fill="#e8262f"/><text x="160" y="23">STEP 03</text>
    <polygon points="189,6 244,6 256,20 244,34 189,34 201,20" fill="#1d3f80"/><text x="223" y="23">STEP 04</text>
    <polygon points="252,6 307,6 319,20 307,34 252,34 264,20" fill="#e8262f"/><text x="286" y="23">STEP 05</text>
  </svg>
  <svg class="abs" style="left:22px;top:122px" width="335" height="16"><g stroke="#bbb" stroke-width=".6"><line x1="34" y1="0" x2="34" y2="12"/><line x1="97" y1="0" x2="97" y2="12"/><line x1="160" y1="0" x2="160" y2="12"/><line x1="223" y1="0" x2="223" y2="12"/><line x1="286" y1="0" x2="286" y2="12"/></g></svg>
  <div class="abs center" style="left:30px;top:140px;width:320px;display:flex;justify-content:space-between">
    <div style="width:54px"><p style="font-size:5px;font-weight:700;color:var(--navy)">Project name</p><p class="tiny" style="font-size:3.9px">Lorem Ipsum is simply dummy unknown printer took a galley of type and scrambled it to make</p></div>
    <div style="width:54px"><p style="font-size:5px;font-weight:700;color:var(--navy)">Project name</p><p class="tiny" style="font-size:3.9px">Lorem Ipsum is simply dummy unknown printer took a galley of type and scrambled it to make</p></div>
    <div style="width:54px"><p style="font-size:5px;font-weight:700;color:var(--navy)">Project name</p><p class="tiny" style="font-size:3.9px">Lorem Ipsum is simply dummy unknown printer took a galley of type and scrambled it to make</p></div>
    <div style="width:54px"><p style="font-size:5px;font-weight:700;color:var(--navy)">Project name</p><p class="tiny" style="font-size:3.9px">Lorem Ipsum is simply dummy unknown printer took a galley of type and scrambled it to make</p></div>
    <div style="width:54px"><p style="font-size:5px;font-weight:700;color:var(--navy)">Project name</p><p class="tiny" style="font-size:3.9px">Lorem Ipsum is simply dummy unknown printer took a galley of type and scrambled it to make</p></div>
  </div>
  <span class="edge-dot"></span><span class="edge-name">Ledger Paladin</span><span class="page-no">38</span>
</section>

<!-- 39 Q&A -->
<section class="slide">
  <h2 class="abs title center" style="left:0;width:370px;top:18px;font-size:15px">Q&amp;A Slide<span class="bar" style="margin:5px auto 0"></span></h2>
  <div class="abs" style="left:45px;top:60px;display:grid;grid-template-columns:150px 150px;column-gap:25px;row-gap:14px">
    <div style="display:flex;gap:8px"><span style="flex:none;width:18px;height:18px;border-radius:3px;background:var(--navy);color:#fff;font-size:9px;font-weight:800;text-align:center;line-height:18px">Q</span><p class="tiny" style="font-size:4px">Lorem Ipsum is simply dummy unknown printer took a galley of type and scrambled it to make.</p></div>
    <div style="display:flex;gap:8px"><span style="flex:none;width:18px;height:18px;border-radius:3px;background:var(--red);color:#fff;font-size:9px;font-weight:800;text-align:center;line-height:18px">A</span><p class="tiny" style="font-size:4px">type and scrambled it to make. Lorem Ipsum is simply unknown printer took a galley of type.</p></div>
    <div style="display:flex;gap:8px"><span style="flex:none;width:18px;height:18px;border-radius:3px;background:var(--navy);color:#fff;font-size:9px;font-weight:800;text-align:center;line-height:18px">Q</span><p class="tiny" style="font-size:4px">Lorem Ipsum is simply dummy unknown printer took a galley of type and scrambled it to make.</p></div>
    <div style="display:flex;gap:8px"><span style="flex:none;width:18px;height:18px;border-radius:3px;background:var(--red);color:#fff;font-size:9px;font-weight:800;text-align:center;line-height:18px">A</span><p class="tiny" style="font-size:4px">type and scrambled it to make. Lorem Ipsum is simply unknown printer took a galley of type.</p></div>
    <div style="display:flex;gap:8px"><span style="flex:none;width:18px;height:18px;border-radius:3px;background:var(--navy);color:#fff;font-size:9px;font-weight:800;text-align:center;line-height:18px">Q</span><p class="tiny" style="font-size:4px">Lorem Ipsum is simply dummy unknown printer took a galley of type and scrambled it to make.</p></div>
    <div style="display:flex;gap:8px"><span style="flex:none;width:18px;height:18px;border-radius:3px;background:var(--red);color:#fff;font-size:9px;font-weight:800;text-align:center;line-height:18px">A</span><p class="tiny" style="font-size:4px">type and scrambled it to make. Lorem Ipsum is simply unknown printer took a galley of type.</p></div>
    <div style="display:flex;gap:8px"><span style="flex:none;width:18px;height:18px;border-radius:3px;background:var(--navy);color:#fff;font-size:9px;font-weight:800;text-align:center;line-height:18px">Q</span><p class="tiny" style="font-size:4px">Lorem Ipsum is simply dummy unknown printer took a galley of type and scrambled it to make.</p></div>
    <div style="display:flex;gap:8px"><span style="flex:none;width:18px;height:18px;border-radius:3px;background:var(--red);color:#fff;font-size:9px;font-weight:800;text-align:center;line-height:18px">A</span><p class="tiny" style="font-size:4px">type and scrambled it to make. Lorem Ipsum is simply unknown printer took a galley of type.</p></div>
  </div>
  <span class="edge-dot"></span><span class="edge-name">Ledger Paladin</span><span class="page-no">39</span>
</section>

<!-- 40 thank you -->
<section class="slide">
  <div class="brand" style="left:54px;top:55px"><span class="brand-dot"></span><span class="brand-name">Ledger Paladin</span></div>
  <div class="abs" style="left:43px;top:78px;width:117px;height:18px;background:var(--navy);display:flex;align-items:center;gap:8px;padding-left:8px;color:#fff;font-size:4.5px"><span style="width:8px;height:8px;border-radius:50%;border:1px solid #fff"></span>www.ledgerpaladinx.com</div>
  <div class="abs" style="left:43px;top:96px;width:117px;height:70px;background:#fff;box-shadow:0 1px 5px rgba(0,0,0,.12)"></div>
  <div class="abs" style="left:51px;top:106px;display:flex;gap:8px;align-items:center;font-size:4px;color:#888"><span style="width:8px;height:8px;border-radius:50%;background:var(--navy)"></span><span>How to write your<br>Company adress</span></div>
  <div class="abs" style="left:51px;top:139px;display:flex;gap:8px;align-items:center;font-size:4.2px;color:#888"><svg width="8" height="6"><rect x=".5" y=".5" width="7" height="5" fill="none" stroke="#1d3f80"/><path d="M.5 .5 L4 3.5 L7.5 .5" fill="none" stroke="#1d3f80"/></svg><span>info@ledgerpaladinx.com</span></div>
  <h2 class="abs title" style="left:200px;top:96px;font-size:22px;letter-spacing:.3px">THANK YOU</h2>
</section>

<!-- 41 questions -->
<section class="slide">
  <svg class="abs" style="left:85px;top:30px" width="220" height="160" viewBox="0 0 220 160">
    <polygon points="10,20 200,5 185,125 110,120 90,150 85,120 20,125" fill="none" stroke="#1d3f80" stroke-width="1.5"/>
    <polygon points="4,28 210,14 192,118 112,112 92,145 88,112 14,118" fill="none" stroke="#e8262f" stroke-width="1.5"/>
    <polygon points="22,30 195,22 180,112 110,108 94,134 88,108 30,112" fill="#fff"/>
  </svg>
  <div class="abs" style="left:150px;top:33px;width:40px;height:3px;background:var(--red)"></div>
  <div class="abs" style="left:110px;top:45px;width:18px;height:2px;background:var(--navy)"></div>
  <h2 class="abs title center" style="left:0;right:0;top:96px;font-size:21px;font-weight:600">Questions?</h2>
</section>

</main>
</body>
</html>
```